Sample Box for Collegiate Alumni Fundraising

We are a screen printing and embroidery company. Our core services are 1) printing & embroidery on apparel (t-shirts, hoodies etc) 2) promo products like mugs, stickers and 3) fulfillment (shipping orders to individuals that have placed orders.
I would like a sample box designed for our specific target market - College and university alumni giving offices. These offices are in charge of running fundraising campaigns. The two main types of campaigns are Giving Day (each school choses their own unique date but most are in the spring) and Open Hand Week (this is a set date each year which occurs the Tuesday after Thanksgiving). Many schools host their own day as well as participate in Open Hand Week. Oftentimes we are tasked with research and tracking down the right product for each campaign.
I have attached two examples that we had created for running clubs. I am open to both real photos or illustrations. I do not want to match these examples, I just want to demonstrate the general design of a sample box.
I do want to highlight our services on side panels like the examples. Printing, Fulfillment, Product Options

```html
<!DOCTYPE html>
<html lang="en">
<head>
<meta charset="utf-8">
<title>Alumni Campaign Sample Box – Panels</title>
<link rel="stylesheet" href="https://fonts.googleapis.com/css2?family=Fraunces:ital,opsz,wght@0,9..144,600;1,9..144,500&family=Lato:wght@400;700;900&display=swap">
<style>
  :root {
    --navy: #1d3f7c;
    --orange: #d8612f;
    --paper: #f6f5f1;
    --cream: #f3ebe0;
    --bg: #d3d3d5;
    --ink-soft: #3f5a8c;
  }
  * { box-sizing: border-box; margin: 0; padding: 0; }
  html, body { width: 1200px; height: 1200px; overflow: hidden; }
  body { background: var(--bg); font-family: "Lato", sans-serif; color: var(--navy); position: relative; }
  .panel { position: absolute; background: var(--paper); box-shadow: 0 2px 10px rgba(0,0,0,.08); }

  /* Lid top */
  .lid-top { left: 40px; top: 40px; width: 600px; height: 640px; background: linear-gradient(180deg, var(--cream) 0%, var(--paper) 70%); overflow: hidden; }
  .brand { position: absolute; left: 32px; top: 30px; display: flex; align-items: center; gap: 8px; font-weight: 900; font-size: 15px; letter-spacing: .5px; text-transform: uppercase; color: var(--navy); }
  .brand-square { width: 14px; height: 14px; background: var(--navy); }
  .lid-headline { position: absolute; left: 60px; top: 80px; font-family: "Fraunces", serif; font-weight: 600; font-size: 62px; line-height: 1.02; color: var(--navy); }
  .campus-art { position: absolute; left: 30px; right: 30px; top: 260px; bottom: 30px; border-radius: 4px; background: linear-gradient(180deg, #efe6d9 0%, #e4e6ee 60%, #dfe3ec 100%); }

  /* Outer front */
  .outer-front { left: 40px; top: 690px; width: 600px; height: 240px; display: grid; grid-template-columns: 1fr 2px 1fr 2px 1fr; align-items: center; padding: 0 30px; }
  .feature { text-align: center; }
  .feature svg { width: 74px; height: 60px; stroke: var(--orange); fill: none; stroke-width: 3; stroke-linejoin: round; stroke-linecap: round; }
  .feature-label { margin-top: 12px; font-size: 14px; letter-spacing: 1px; text-transform: uppercase; line-height: 1.25; color: var(--navy); }
  .divider { width: 2px; height: 110px; background: var(--navy); }

  /* Inner lid */
  .inner-lid { left: 680px; top: 40px; width: 480px; height: 560px; text-align: center; padding: 110px 40px 0; }
  .inner-headline { font-family: "Fraunces", serif; font-weight: 600; font-size: 38px; line-height: 1.15; }
  .rule { width: 90px; height: 3px; background: var(--orange); margin: 22px auto; }
  .inner-copy { font-size: 15px; line-height: 1.6; color: var(--ink-soft); }
  .product-icons { display: flex; justify-content: center; gap: 26px; margin-top: 44px; }
  .product-icons svg { width: 40px; height: 40px; stroke: var(--navy); fill: none; stroke-width: 2; stroke-linejoin: round; stroke-linecap: round; }

  /* Inner front */
  .inner-front { left: 680px; top: 620px; width: 480px; height: 310px; padding: 40px 36px; }
  .tagline { font-family: "Fraunces", serif; font-size: 26px; line-height: 1.2; }
  .tagline em { display: block; color: var(--orange); font-style: italic; font-weight: 500; }
  .kit-art { position: absolute; right: 36px; top: 120px; width: 130px; height: 110px; border-radius: 4px; background: linear-gradient(135deg, #f7e1d5, #efcdb9); }
  .kit-title { position: absolute; left: 36px; bottom: 74px; font-weight: 900; font-size: 34px; }
  .kit-sub { position: absolute; left: 36px; bottom: 44px; font-size: 16px; }

  /* Side band */
  .side-band { left: 40px; top: 950px; width: 1120px; height: 210px; background: var(--navy); color: #fff; padding: 44px 50px; }
  .side-title { font-size: 34px; line-height: 1.15; font-weight: 400; }
  .side-sub { margin-top: 12px; font-size: 16px; opacity: .85; }
  .needle-art { position: absolute; right: 60px; top: 35px; width: 120px; height: 140px; border-radius: 4px; background: linear-gradient(160deg, #e0703c, #b94f24); }
</style>
</head>
<body>

<section class="panel lid-top">
  <div class="brand"><span class="brand-square"></span>Harbor Line Graphics</div>
  <h1 class="lid-headline">campaigns that<br>inspire giving</h1>
  <div class="campus-art" role="img" aria-label="Line illustration of alumni in branded apparel celebrating in front of a campus building"></div>
</section>

<section class="panel outer-front">
  <div class="feature">
    <svg viewBox="0 0 74 60"><path d="M14 20 L37 10 L60 20 L60 46 L37 56 L14 46 Z"/><path d="M14 20 L37 30 L60 20"/><path d="M37 30 V56"/></svg>
    <div class="feature-label">No<br>Inventory</div>
  </div>
  <div class="divider"></div>
  <div class="feature">
    <svg viewBox="0 0 74 60"><rect x="10" y="8" width="54" height="36" rx="3"/><path d="M30 52 H44 M37 44 V52"/></svg>
    <div class="feature-label">Online<br>Stores</div>
  </div>
  <div class="divider"></div>
  <div class="feature">
    <svg viewBox="0 0 74 60"><rect x="6" y="14" width="38" height="28"/><path d="M44 22 H58 L68 32 V42 H44 Z"/><circle cx="18" cy="46" r="5"/><circle cx="56" cy="46" r="5"/></svg>
    <div class="feature-label">Direct<br>Shipping</div>
  </div>
</section>

<section class="panel inner-lid">
  <h2 class="inner-headline">Make every<br>donor feel connected.</h2>
  <div class="rule"></div>
  <p class="inner-copy">We help alumni offices create branded<br>merchandise experiences that inspire giving,<br>celebrate school pride, and simplify fulfillment.</p>
  <div class="product-icons">
    <svg viewBox="0 0 40 40"><path d="M14 6 L4 12 L8 19 L12 17 V35 H28 V17 L32 19 L36 12 L26 6 Q20 11 14 6 Z"/></svg>
    <svg viewBox="0 0 40 40"><path d="M10 5 H19 V24 L24 30 Q26 35 21 36 L12 33 Q8 31 10 26 Z"/><path d="M22 5 H30 V24 L34 30"/></svg>
    <svg viewBox="0 0 40 40"><path d="M6 26 Q6 10 20 10 Q32 10 32 24 Z"/><path d="M6 26 H36"/></svg>
    <svg viewBox="0 0 40 40"><path d="M14 8 Q20 2 26 8 L34 14 V34 H6 V14 Z"/><path d="M14 8 Q20 16 26 8"/><rect x="14" y="24" width="12" height="7"/></svg>
    <svg viewBox="0 0 40 40"><path d="M13 3 L20 16 L27 3"/><circle cx="20" cy="26" r="10"/><circle cx="20" cy="26" r="4"/></svg>
  </div>
</section>

<section class="panel inner-front">
  <p class="tagline">You lead the campaign.<em>We handle the details.</em></p>
  <div class="kit-art" role="img" aria-label="Line illustration of an open box filled with a t-shirt, bottle and pennant"></div>
  <h3 class="kit-title">Campaign Kits</h3>
  <p class="kit-sub">Shipped directly to alumni supporters</p>
</section>

<section class="panel side-band">
  <h3 class="side-title">Printing<br>&amp; Embroidery</h3>
  <p class="side-sub">Custom apparel for alumni, donors, students &amp; staff</p>
  <div class="needle-art" role="img" aria-label="Illustration of an embroidery needle and thread"></div>
</section>

</body>
</html>
```